Sci-Fi Safari-E-Book Cover

We're looking for a cover for a science fiction novel that will be sold as an E-Book. The theme of the book includes a safari on an alien world, where the main goal is to kill a red lion (which is the same as African lions on this world, only bigger).

The background will be preferably black, with most of the cover taken up (in the middle) by an image of the lion peering straight out from the darkness. Not much will be visible, probably just the glowing eyes, a little bit of the nose, and some of the fangs.

At the very top we'd like the cover to include the series' title: "Under Watch."

And just below that in somewhat larger letters we'd like it to say "The Fenway Baron."

At the bottom we want it to say "Derek Asholt," in smaller letters. We're thinking we want a red font, and perhaps highlighted by some sort of lighting effect. We're not completely decided on that, however.

Thank you for your interest
Updates

Hello, we haven't previously clarified this, but we'd like the ratio for this book cover to 1.6, or near that.

Thank you

Target Market(s)

English science fiction novel readers.

Requirements
Must have
• Text that says (in this order):

Under Watch (at the top of the page)
The Fenway Baron (just below "Under Watch", with slightly larger font)

Derek Asholt (at the bottom of the page)
-
Black background
Lion face peering out of shadows
Lion's eyes with slanted irises
Visible Fangs
-
Image details: 1.6 ratio
Nice to have
• More of a photo-realistic feel to the lion, rather than art-like feel.

Some sort of lighting affect around the text "Under Watch" & "The Fenway Baron."

```html
<!DOCTYPE html>
<html lang="en">
<head>
<meta charset="utf-8">
<title>Under Watch – The Fenway Baron – Cover Spread</title>
<link href="https://fonts.googleapis.com/css2?family=Black+Ops+One&family=Oswald:wght@300;600&family=Cabin:wght@400&family=Marcellus&display=swap" rel="stylesheet">
<style>
  :root {
    --stage: #ececec;
    --cover-black: #070707;
    --title-red: #b3151b;
    --title-glow: #ff2a2a;
    --subtitle-pink: #f1d2d2;
    --text-white: #f4f4f4;
    --placeholder-grey: #d9d9d9;
    --placeholder-ink: #222;
    --lion-gold: #c9a24a;
    --lion-brown: #6b4a1c;
  }
  * { margin: 0; padding: 0; box-sizing: border-box; }
  html, body { width: 1200px; height: 800px; overflow: hidden; }
  body { background: var(--stage); position: relative; font-family: "Cabin", sans-serif; }

  .cover {
    position: absolute; top: 96px; width: 380px; height: 608px;
    background: var(--cover-black); color: var(--text-white); overflow: hidden;
  }
  .back-cover { left: 170px; text-align: center; }
  .front-cover { left: 650px; }
  .spine {
    position: absolute; left: 580px; top: 96px; width: 40px; height: 608px;
    background: var(--cover-black);
    display: flex; flex-direction: column; align-items: center; padding: 14px 0;
  }

  .series-title {
    font-family: "Black Ops One", sans-serif; text-transform: uppercase;
    color: var(--title-red); -webkit-text-stroke: 1px #ffd0d0;
    text-shadow: 0 0 6px var(--title-glow), 0 0 14px var(--title-glow);
    letter-spacing: 2px; white-space: nowrap;
  }

  /* Back cover */
  .back-cover .author-credit {
    font-family: "Marcellus", serif; font-size: 11px; letter-spacing: 0.5px;
    text-align: right; padding: 28px 30px 0 0;
  }
  .back-cover .series-title { font-size: 46px; margin-top: 4px; }
  .back-cover .book-title {
    font-family: "Oswald", sans-serif; font-weight: 300; font-size: 21px;
    letter-spacing: 5px; color: var(--subtitle-pink); margin-top: 6px; text-transform: uppercase;
  }
  .blurb {
    font-size: 10.4px; line-height: 1.45; padding: 0 22px; margin-top: 22px;
  }
  .back-footer {
    position: absolute; left: 0; right: 0; bottom: 40px;
    display: flex; justify-content: space-between; padding: 0 22px;
  }
  .placeholder-box {
    width: 106px; height: 50px; background: var(--placeholder-grey); color: var(--placeholder-ink);
    display: flex; align-items: center; justify-content: center;
    font-weight: 600; font-size: 12px;
  }
  .copyright {
    position: absolute; bottom: 14px; width: 100%; font-size: 6px; letter-spacing: 0.5px;
    font-family: "Marcellus", serif; text-transform: uppercase;
  }

  /* Spine */
  .spine .series-title {
    writing-mode: vertical-rl; font-size: 26px; letter-spacing: 4px;
  }
  .spine .spine-author {
    writing-mode: vertical-rl; font-family: "Marcellus", serif; font-size: 8px;
    letter-spacing: 1px; color: var(--text-white); margin-top: 24px;
  }

  /* Front cover */
  .lion-art {
    position: absolute; left: 70px; top: 0; width: 310px; height: 608px;
    background:
      radial-gradient(ellipse 55% 45% at 55% 52%, var(--lion-gold) 0%, #a47d35 40%, var(--lion-brown) 70%, transparent 100%),
      radial-gradient(ellipse 70% 60% at 75% 30%, #8a6629 0%, transparent 70%);
  }
  .front-cover .series-title {
    position: absolute; top: 18px; width: 100%; text-align: center; font-size: 48px;
  }
  .front-cover .book-title {
    position: absolute; top: 488px; width: 100%; text-align: center;
    font-family: "Oswald", sans-serif; font-weight: 600; font-size: 40px; letter-spacing: 0.5px;
    color: var(--text-white); text-transform: uppercase;
    text-shadow: 0 0 2px #7a0d0d, 2px 2px 0 #5a0a0a;
  }
  .front-cover .author-name {
    position: absolute; top: 560px; width: 100%; text-align: center;
    font-family: "Marcellus", serif; font-size: 17px; letter-spacing: 0.5px;
    color: var(--text-white); text-transform: uppercase; font-weight: bold;
  }
</style>
</head>
<body>

  <section class="cover back-cover">
    <p class="author-credit">DEREK ASHOLT'S</p>
    <h2 class="series-title">Under Watch</h2>
    <p class="book-title">The Fenway Baron</p>
    <p class="blurb">Lorem ipsum dolor sit amet, consectetur adipisicing elit, sed do eiusmod tempor incididunt ut labore et dolore magna aliqua. Ut enim ad minim veniam, quis nostrud exercitation. Lorem ipsum dolor sit amet, consectetur adipisicing elit, sed do eiusmod tempor incididunt ut labore et dolore magna aliqua. Ut enim ad minim veniam, quis nostrud exercitation. Lorem ipsum dolor sit amet, consectetur adipisicing elit, sed do eiusmod tempor incididunt ut labore et dolore magna aliqua. Ut enim ad minim veniam, quis nostrud exercitation. Lorem ipsum dolor sit amet, consectetur adipisicing elit, sed do eiusmod tempor incididunt ut labore et dolore magna aliqua. Ut enim ad minim veniam, quis nostrud exercitation. Lorem ipsum dolor sit amet, consectetur adipisicing elit, sed do eiusmod tempor incididunt ut labore et dolore magna aliqua. Ut enim ad minim veniam, quis nostrud exercitation. Lorem ipsum dolor sit amet, consectetur adipisicing elit, sed do eiusmod tempor incididunt ut labore et dolore magna aliqua. Ut enim ad minim veniam, quis nostrud exercitation. Lorem ipsum dolor sit amet, consectetur adipisicing elit.</p>
    <div class="back-footer">
      <div class="placeholder-box">LOGO</div>
      <div class="placeholder-box">ISBN</div>
    </div>
    <p class="copyright">Copyright © 2012 by Derek Asholt</p>
  </section>

  <section class="spine">
    <span class="series-title">Under Watch</span>
    <span class="spine-author">DEREK ASHOLT</span>
  </section>

  <section class="cover front-cover">
    <div class="lion-art" role="img" aria-label="Illustration of a snarling golden lion with a red eye and bared fangs emerging from the darkness"></div>
    <h1 class="series-title">Under Watch</h1>
    <p class="book-title">The Fenway Baron</p>
    <p class="author-name">Derek Asholt</p>
  </section>

</body>
</html>
```